Varden Ridge Concrete Pumping needs a logo design and is in the concrete industry

A creative design for this Varden Ridge Concrete Pumping business. Using a trailer mounted line pump, not a boom pump.
Colour to be used is orange and a mix of white or black writing.
Target Market(s)
General Public, anyone
Industry/Entity Type
Concrete
Contact Information for Business Card
Varden Ridge Concrete Pumping
Brennan Holloway
PO BOX 47
Marlowe Creek VIC 3288
Phone: 0491552083
Email: Holloway@postwren.com.au
Colors
f37122
000000
ffffff
Requirements
Must have
- Details listed
Nice to have
- A great logo
Should not have
- anything silly

```html
<!DOCTYPE html>
<html lang="en">
<head>
<meta charset="utf-8">
<title>Varden Ridge Concrete Pumping – Business Card</title>
<link href="https://fonts.googleapis.com/css2?family=Audiowide&family=Roboto:wght@400;500&display=swap" rel="stylesheet">
<style>
  :root {
    --orange: #f37122;
    --black: #141414;
    --white: #ffffff;
    --stage: #cfa87c;
    --concrete-light: #8d929a;
    --concrete-dark: #5d626a;
    --emboss: #45484d;
  }
  html, body {
    margin: 0;
    padding: 0;
    width: 1181px;
    height: 1200px;
    overflow: hidden;
    background: var(--stage);
  }
  .canvas {
    position: relative;
    width: 1181px;
    height: 1200px;
  }
  .card {
    position: absolute;
    left: 230px;
    width: 722px;
    border-radius: 22px;
    overflow: hidden;
  }
  .card-front {
    top: 101px;
    height: 454px;
    background: var(--black);
    font-family: "Roboto", sans-serif;
    color: var(--white);
  }
  .card-back {
    top: 642px;
    height: 455px;
    background: radial-gradient(ellipse at 55% 35%, var(--concrete-light), var(--concrete-dark));
  }
  .name-accent {
    position: absolute;
    left: 41px;
    top: 65px;
    width: 7px;
    height: 58px;
    background: var(--orange);
  }
  .person-name {
    position: absolute;
    left: 59px;
    top: 68px;
    margin: 0;
    font-family: "Audiowide", sans-serif;
    font-weight: 400;
    font-size: 24px;
    letter-spacing: 0.5px;
    color: var(--white);
  }
  .job-title {
    position: absolute;
    left: 58px;
    top: 96px;
    margin: 0;
    font-size: 19px;
    color: var(--orange);
  }
  .contact {
    position: absolute;
    left: 41px;
    top: 288px;
    margin: 0;
    padding: 0;
    list-style: none;
    font-size: 17px;
    line-height: 23px;
  }
  .contact li {
    position: relative;
    padding-left: 23px;
    margin-bottom: 8px;
  }
  .contact svg {
    position: absolute;
    left: 0;
    top: 4px;
    width: 14px;
    height: 14px;
    fill: var(--orange);
  }
  .front-band {
    position: absolute;
    left: 0;
    bottom: 0;
    width: 722px;
    height: 40px;
  }
  .company-name {
    position: absolute;
    right: 22px;
    top: 318px;
    margin: 0;
    text-align: right;
    font-family: "Roboto", sans-serif;
    font-weight: 500;
    font-size: 27px;
    line-height: 32px;
    color: var(--white);
  }
  .company-mark {
    position: absolute;
    right: 24px;
    top: 276px;
    width: 26px;
    height: 26px;
    background: var(--orange);
  }
  .back-name {
    position: absolute;
    left: 0;
    right: 0;
    top: 255px;
    margin: 0;
    text-align: center;
    font-family: "Roboto", sans-serif;
    font-weight: 500;
    font-size: 42px;
    line-height: 48px;
    color: var(--emboss);
  }
</style>
</head>
<body>
<main class="canvas">

  <section class="card card-front" aria-label="Business card front">
    <div class="name-accent"></div>
    <h1 class="person-name">Brennan Holloway</h1>
    <p class="job-title">Job Title</p>

    <ul class="contact">
      <li>
        <svg viewBox="0 0 14 14" aria-hidden="true"><path d="M7 0C4.2 0 2.2 2 2.2 4.7 2.2 8 7 14 7 14s4.8-6 4.8-9.3C11.8 2 9.8 0 7 0zm0 6.6A1.9 1.9 0 1 1 7 2.8a1.9 1.9 0 0 1 0 3.8z"/></svg>
        PO BOX 47<br>Marlowe Creek VIC 3288
      </li>
      <li>
        <svg viewBox="0 0 14 14" aria-hidden="true"><path d="M1 4c0-1.5 2.5-2.5 6-2.5S13 2.5 13 4v1.2h-3V4H4v1.2H1z"/><path d="M3 6h8l1.5 6.5h-11z"/></svg>
        0491552083
      </li>
      <li>
        <svg viewBox="0 0 14 14" aria-hidden="true"><path d="M0 3h14v1L7 8 0 4z"/><path d="M0 5.2l7 4 7-4V11H0z"/></svg>
        Holloway@postwren.com.au
      </li>
    </ul>

    <div class="company-mark"></div>
    <p class="company-name">Varden Ridge<br>Concrete Pumping</p>

    <svg class="front-band" viewBox="0 0 722 40" aria-hidden="true">
      <polygon points="370,0 722,0 722,40 348,40" fill="var(--orange)"/>
    </svg>
  </section>

  <section class="card card-back" role="img" aria-label="Business card back: concrete texture with embossed company name">
    <p class="back-name">Varden Ridge<br>Concrete Pumping</p>
  </section>

</main>
</body>
</html>
```